Hardware Brand Packaging Design Project

We require a design for packaging for products in the retail hardware range. Initially this will be for a set of header cards for abrasive sanding discs but we plan to add other items to the range so we are looking for a range of brand elements that can be extended to other types of packaging.
The brand name is "Lumen Ridge" and we are looking for a black or dark grey background with a subtle fine pattern to break up the solid colour. This part of the design needs to be 'expandable' so that it can be used on different pack sizes as we increase the range. Two highlight or complimentary colours will add a bit of impact and become part of the brand style.
For printing purposes we have allowed for 4 colour process plus two spot colours and we have attached one of the header card dielines as a guide.
Target Market(s)
Home owners of both gender in the 25 to 55 age range
Industry/Entity Type
Printing
Requirements
Must have
- *The brand name "Lumen Ridge" should appear in the top left hand corner and we had in mind that the word would be a shiny metal / chrome appearance in could be in the shape of a shield or spear point but are open to any other suggestions.The word can be on one line or one above the other.
*Between the bottom of the hanger hole and the edge of the card is the words ABRASIVES & ACCESSORIES
*We want a performance guarantee device circle / seal or other in the bottom left quartile of the front facing panel. Circle device on attachment shows approx position.
* The right hand 25mm of the card is to be devoted to specific information about the product in the pack. This will be done by an adhered over-sticker ( see attached die-line No 2 )
* 3 line address panel or rear of card - QRV Abrasives, 456 Lane, West Auckland, New Zealand.
* Also somewhere on rear panel "Cut, Quality Checked & Packed in New Zealand from imported materials."
Nice to have
- It would be good, but not essential, to see a rough mock-up of how this design would transfer across to a box approx 80mm across the front, 100mm deep and 250mm high.

```html
<!DOCTYPE html>
<html lang="en">
<head>
<meta charset="utf-8">
<title>Lumen Ridge – Abrasives Header Card</title>
<link rel="stylesheet" href="https://fonts.googleapis.com/css2?family=Arimo:wght@400;700&family=Roboto+Condensed:wght@700&display=swap">
<style>
  :root {
    --page: #ffffff;
    --red-core: #ee2229;
    --red-edge: #b51a20;
    --grey: #5b5c5e;
    --grey-shadow: #141414;
    --dieline: #2ba6df;
    --fold-green: #3fb54a;
    --fold-white: #ffffff;
    --ribbon: #a9abae;
    --ribbon-dark: #8d8f92;
    --gold-light: #ffe34d;
    --gold-dark: #e0a800;
    --text-light: #ffffff;
  }
  * { margin: 0; padding: 0; box-sizing: border-box; }
  html, body {
    width: 1200px; height: 1000px; overflow: hidden;
    background: var(--page);
  }
  .canvas { position: relative; width: 1200px; height: 1000px; }

  .header-card {
    position: absolute; left: 170px; top: 62px;
    width: 930px; height: 858px;
    border-radius: 16px; overflow: hidden;
  }
  .back-panel {
    position: absolute; left: 0; top: 0; width: 100%; height: 606px;
    background: radial-gradient(ellipse 60% 70% at 50% 45%, var(--red-core), var(--red-edge));
  }
  .front-band {
    position: absolute; left: 0; top: 606px; width: 100%; height: 252px;
    background: linear-gradient(180deg, var(--grey-shadow) 0, var(--grey) 34px, var(--grey) 100%);
  }

  .upside-down { position: absolute; transform: rotate(180deg); color: var(--text-light); text-align: center; font-family: "Arimo", Arial, sans-serif; }
  .web-address { left: 175px; top: 136px; width: 580px; font-weight: 700; font-size: 24px; }
  .origin-note { left: 270px; top: 195px; width: 380px; font-size: 17px; line-height: 30px; letter-spacing: 0.6px; }
  .address-panel { left: 5px; top: 292px; width: 266px; font-size: 17px; line-height: 31px; }
  .address-panel .company { font-weight: 700; }

  .range-title {
    position: absolute; left: 230px; top: 622px; width: 470px;
    font-family: "Roboto Condensed", "Arial Narrow", sans-serif; font-weight: 700;
    font-size: 48px; line-height: 46px; color: var(--text-light); text-align: center;
    text-shadow: 2px 3px 4px rgba(0,0,0,0.6);
  }

  .brand-name {
    position: absolute; left: 28px; top: 498px; width: 180px;
    font-family: "Roboto Condensed", "Arial Narrow", sans-serif; font-weight: 700;
    font-size: 40px; line-height: 42px; color: var(--text-light); text-align: center;
  }

  .guarantee-seal {
    position: absolute; left: 37px; top: 677px; width: 158px; height: 158px;
    border-radius: 50%;
    background: radial-gradient(circle at 45% 40%, var(--gold-light), var(--gold-dark));
  }
  .guarantee-text {
    position: absolute; left: 37px; top: 725px; width: 158px; text-align: center;
    font-family: "Roboto Condensed", "Arial Narrow", sans-serif; font-weight: 700;
    color: var(--text-light); text-shadow: 1px 1px 2px rgba(0,0,0,0.4);
  }
  .guarantee-text .top { font-size: 16px; display: block; }
  .guarantee-text .main { font-size: 28px; display: block; line-height: 30px; }

  .ribbon { position: absolute; left: 0; top: 0; }
  .dieline { position: absolute; left: 0; top: 0; }
</style>
</head>
<body>
<div class="canvas">
  <div class="header-card">
    <div class="back-panel"></div>
    <div class="front-band"></div>

    <svg class="ribbon" width="930" height="858" aria-hidden="true">
      <polygon points="58,598 175,598 175,843 116,815 58,843" fill="var(--ribbon)"/>
      <rect x="116" y="598" width="59" height="222" fill="var(--ribbon-dark)"/>
    </svg>

    <div class="upside-down web-address">qrvabrasives.com</div>
    <div class="upside-down origin-note">Cut, Quality Checked &amp; Packed in<br>New Zealand from imported materials.</div>
    <div class="upside-down address-panel">
      <div class="company">QRV Abrasives</div>
      <div>456 Lane</div>
      <div>West Auckland, New Zealand</div>
    </div>

    <div class="brand-name">LUMEN<br>RIDGE</div>

    <div class="guarantee-seal" role="img" aria-label="Gold performance guarantee seal"></div>
    <div class="guarantee-text"><span class="top">PERFORMANCE</span><span class="main">GUARANTEE</span></div>

    <div class="range-title">ABRASIVES<br>&amp; ACCESSORIES</div>
  </div>

  <svg class="dieline" width="1200" height="1000" aria-hidden="true">
    <rect x="170" y="62" width="930" height="858" rx="16" fill="none" stroke="var(--dieline)" stroke-width="2"/>
    <path d="M320 62 Q635 310 950 62" fill="none" stroke="var(--dieline)" stroke-width="2"/>
    <path d="M320 920 Q635 672 950 920" fill="none" stroke="var(--dieline)" stroke-width="2"/>
    <line x1="170" y1="246" x2="1100" y2="246" stroke="var(--fold-green)" stroke-width="1.5" stroke-dasharray="5 5"/>
    <line x1="170" y1="493" x2="1100" y2="493" stroke="var(--fold-white)" stroke-width="2" stroke-dasharray="6 5"/>
    <path d="M368 492 L465 343 Q470 335 480 335 L730 335 Q752 335 752 358 Q752 382 730 385
             Q710 388 700 378 Q680 370 665 390 Q660 420 635 418 Q612 415 610 395 Q600 378 580 382
             Q555 395 535 385 Q518 366 500 368 Q492 372 485 385 L446 455 Q440 470 455 480
             Q468 490 485 492
             Q468 494 455 504 Q440 514 446 529 L485 599 Q492 612 500 616 Q518 618 535 599
             Q555 589 580 602 Q600 606 610 589 Q612 569 635 566 Q660 564 665 594 Q680 614 700 606
             Q710 596 730 599 Q752 602 752 626 Q752 649 730 649 L480 649 Q470 649 465 641 Z"
          fill="none" stroke="var(--dieline)" stroke-width="2"/>
  </svg>
</div>
</body>
</html>
```